Harbor Nest Lodging website, brand new company, that rents rooms out in houses to milleniuls

We have a site right now that is weak as heck! We could use some punching it up. So we want it to be fun and cool, with added items in for social media (just chirpnet now) and anything else you want to throw at us. We do have a “blog” in there dedicated to events (we throw a lot of them) so want to incorporate that. Also have an existing design for a hand out that we want to use as our launching pad for colors… you can deviate from it a bit though.

Target Market(s)

25-40 year olds transitioning to the city from other places in the country. Millennial are the min group

Industry/Entity Type

Real Estate

Coding

Coded - Design and coding required

Number of Pages Required

5+ page

Font styles to use
Sans Serif

Requirements
Must have
• Fun look, same pages as those uploaded, but not necessarily the look and feel of what we have already.
• Follow the content of our posted site www.HarborNestLodging.example
• FOOTER
• LOGO | SITEMAP | SOCIAL LINKS | MAIN CTA REMINDER | CONTACT INFO | COPYRIGHT INFO | TERMS AND CONDITIONS
Nice to have
• Use as many of my graphics as loaded, but feel free to use stock photos as well interlaced. Including both people in their 20’s, 30’s, 40’s, having a fun time or of nice houses, inside and out.

```html
<!DOCTYPE html>
<html lang="en">
<head>
<meta charset="utf-8">
<title>Harbor Nest Lodging</title>
<link href="https://fonts.googleapis.com/css2?family=Open+Sans:ital,wght@0,400;0,600;0,700;1,400&family=Raleway:wght@500;600;700&display=swap" rel="stylesheet">
<style>
:root{
  --blue:#1a5fb4;
  --blue-dark:#154f99;
  --blue-foot-top:#2f73c8;
  --blue-foot-bot:#1a55ad;
  --ink:#3d3d3d;
  --text:#555;
  --muted:#8a8a8a;
  --rule:#cfcfcf;
  --panel:#f2f2f2;
  --bar:#4a4a4a;
  --white:#fff;
}
*{box-sizing:border-box;margin:0;padding:0}
html,body{width:1200px;height:2287px;overflow:hidden;background:var(--white)}
body{position:relative;font-family:"Open Sans",Arial,sans-serif;color:var(--text)}
.abs{position:absolute}

/* header */
.top-rule{left:0;top:0;width:1200px;height:4px;background:var(--blue)}
.site-header{left:0;top:4px;width:1200px;height:116px;background:var(--white)}
.brand{left:160px;top:26px;width:190px;font-family:"Raleway",sans-serif;font-weight:700;color:var(--blue);font-size:25px;line-height:27px;letter-spacing:.5px;text-transform:uppercase;display:flex;align-items:center;gap:10px}
.brand-mark{width:14px;height:14px;background:var(--blue);flex:none}
.call{left:914px;top:14px;display:flex;align-items:center;gap:10px;font-size:13px;color:var(--ink);line-height:18px}
.call strong{font-weight:700;display:block}
.call svg{width:34px;height:34px}
.main-nav{left:409px;top:74px;width:640px;height:20px;font-family:"Raleway",sans-serif;font-size:12px;font-weight:600;color:var(--ink);letter-spacing:.3px}
.main-nav a{position:absolute;top:0;color:inherit;text-decoration:none;white-space:nowrap}
.main-nav a.active{color:var(--blue)}

/* hero */
.photo{background:#999}
.hero-kitchen{left:0;top:120px;width:630px;height:453px;background:linear-gradient(120deg,#b8764a 0%,#d9c9a8 45%,#eef0ea 70%,#a86844 100%)}
.hero-bed1{left:634px;top:120px;width:281px;height:225px;background:linear-gradient(160deg,#8a7a64,#c9b79a 60%,#6e5b45)}
.hero-living{left:634px;top:349px;width:281px;height:224px;background:linear-gradient(160deg,#8c5a3a,#d2b796 55%,#8a3f2a)}
.hero-bed2{left:919px;top:120px;width:281px;height:453px;background:linear-gradient(180deg,#9a6a3e 0%,#b8c5c4 30%,#6e7288 70%,#d8d8d8 100%)}
.hero-banner{left:0;top:485px;width:607px;height:52px;background:rgba(26,95,180,.88);color:var(--white)}
.hero-banner .arrows{position:absolute;left:14px;top:14px;width:30px;height:24px}
.hero-banner p{position:absolute;left:0;width:607px;top:13px;text-align:center;padding-left:70px;font-family:"Raleway",sans-serif;font-size:21px;font-weight:500;letter-spacing:.5px}
.hero-banner b{font-weight:700}
.hero-banner small{font-size:10px;font-style:italic}

/* section titles */
.section-title{font-family:"Raleway",sans-serif;font-weight:600;color:var(--ink);font-size:23px;letter-spacing:.5px;text-transform:uppercase;white-space:nowrap}
.section-title em{font-style:normal;color:var(--blue)}
.title-rule{height:2px;background:var(--rule)}
.title-rule::after{content:"";position:absolute;left:50%;top:-2px;width:42px;height:5px;margin-left:-21px;background:var(--blue)}

/* welcome */
.welcome-title{left:0;top:620px;width:1200px;text-align:center}
.welcome-rule{left:442px;top:664px;width:400px}
.welcome-copy{left:226px;top:691px;width:750px;text-align:center;font-size:10.5px;line-height:20px;color:var(--ink)}
.btn{display:inline-block;background:var(--blue);color:var(--white);text-decoration:none;font-weight:700;text-transform:uppercase}
.btn-contact{left:534px;top:795px;width:132px;height:42px;line-height:42px;text-align:center;font-size:14px;letter-spacing:.5px}

/* amenities */
.amenities{left:0;top:880px;width:1200px;height:334px;background:var(--panel);border-top:1px solid #e2e2e2;border-bottom:1px solid #e2e2e2}
.amenities-photo{left:0;top:0;width:640px;height:332px;background:linear-gradient(90deg,#6e5a44 0%,#a78f74 35%,#d7cbbb 65%,rgba(242,242,242,0) 100%)}
.amenities-title{left:508px;top:60px;font-size:21px}
.amenities-title sup{font-size:11px}
.amenities-rule{left:508px;top:100px;width:347px;height:1px;background:var(--rule)}
.amenity-list{list-style:none;font-family:"Raleway",sans-serif;font-size:12px;color:var(--text);line-height:15px}
.amenity-list li{position:relative;padding-left:19px;margin-bottom:12px}
.amenity-list li svg{position:absolute;left:0;top:2px;width:11px;height:11px}
.amenity-col1{left:514px;top:127px;width:270px}
.amenity-col2{left:790px;top:127px;width:260px}

/* highlights */
.highlight{top:1270px;width:270px}
.highlight h3{font-size:21px}
.highlight .rule{position:relative;margin-top:12px;height:2px;background:var(--rule)}
.highlight .rule::after{content:"";position:absolute;left:0;top:-1px;width:56px;height:4px;background:var(--ink)}
.highlight .photo{margin-top:26px;height:150px}
.highlight p{margin-top:16px;font-size:10.5px;line-height:20.5px;color:var(--ink)}
.btn-more{margin-top:14px;width:94px;height:34px;line-height:34px;font-size:10px;text-align:center}
.btn-more svg{width:9px;height:9px;vertical-align:-1px;margin-left:2px}
.col-home{left:160px}.col-events{left:464px}.col-latest{left:767px}
.photo-home{background:linear-gradient(150deg,#8c5a3a,#d2b796 55%,#8a3f2a)}
.photo-events{background:linear-gradient(150deg,#4b5a6b,#a8b8c4 50%,#3e4a3a)}
.photo-latest{background:linear-gradient(170deg,#8e6a4a,#b8c5c4 40%,#5d6480 80%)}

/* fans */
.fans{left:0;top:1685px;width:1200px;height:346px;background:var(--panel);border-top:1px solid #e2e2e2}
.fans-title{left:0;top:38px;width:1200px;text-align:center}
.fans-rule{left:434px;top:79px;width:332px}
.avatar{width:144px;height:144px;border-radius:50%;border:5px solid var(--white);box-shadow:0 0 0 1px #d4d4d4;background:linear-gradient(160deg,#e6d6bf,#c79e77 60%,#8d6a4f)}
.avatar-1{left:161px;top:126px}
.avatar-2{left:628px;top:126px}
.fan-name{font-family:"Raleway",sans-serif;font-weight:700;color:var(--blue);font-size:13px;width:144px;text-align:center;top:292px}
.fan-1{left:161px}.fan-2{left:628px}
.quote{font-style:italic;font-size:10.3px;line-height:22px;color:var(--ink)}
.quote-1{left:323px;top:116px;width:290px}
.quote-2{left:788px;top:116px;width:290px}

/* footer */
.site-footer{left:0;top:2031px;width:1200px;height:205px;background:linear-gradient(180deg,var(--blue-foot-top),var(--blue-foot-bot));color:var(--white)}
.footer-brand{left:160px;top:34px;width:180px;font-family:"Raleway",sans-serif;font-weight:700;font-size:21px;line-height:23px;text-transform:uppercase;display:flex;align-items:center;gap:8px}
.footer-brand span.mark{width:12px;height:12px;background:var(--white);flex:none}
.footer-about{left:160px;top:103px;width:200px;font-size:10.5px;line-height:17px}
.footer-col h4{font-family:"Raleway",sans-serif;font-size:14px;font-weight:600;text-transform:uppercase;letter-spacing:.5px;margin-bottom:6px}
.footer-col a{display:block;color:var(--white);text-decoration:none;font-size:11px;line-height:22.5px}
.col-resources{left:427px;top:28px}
.col-support{left:612px;top:28px}
.col-news{left:795px;top:28px;width:245px}
.col-news p{font-size:11px;margin-bottom:12px}
.email-field{display:block;width:241px;height:32px;border:1px solid #dcdcdc;background:var(--white);padding-left:12px;font-family:inherit;font-size:10px;color:#777;line-height:30px}
.btn-subscribe{display:block;margin-top:10px;width:117px;height:38px;line-height:38px;text-align:center;background:var(--bar);color:var(--white);font-weight:700;font-size:12px;text-transform:uppercase}

.bottom-bar{left:0;top:2236px;width:1200px;height:51px;background:var(--bar);color:var(--white)}
.copyright{left:163px;top:17px;font-size:11px}
.social{left:875px;top:10px;display:flex;gap:6px}
.social a{display:block;width:29px;height:29px;border:1.5px solid var(--white);border-radius:50%}
</style>
</head>
<body>

<div class="abs top-rule"></div>
<header class="abs site-header">
  <div class="abs brand"><span class="brand-mark"></span><span>Harbor Nest Lodging</span></div>
  <div class="abs call">
    <svg viewBox="0 0 34 34" aria-hidden="true"><circle cx="17" cy="17" r="15.5" fill="none" stroke="#1a5fb4" stroke-width="1.5"/><path d="M12.5 10.5c1-.6 1.6-.4 2.2.6l1.2 2.2c.4.8.2 1.4-.5 1.9l-.9.6c.8 1.9 2 3.2 3.8 4l.6-.9c.5-.7 1.1-.9 1.9-.5l2.2 1.2c1 .6 1.2 1.2.6 2.2-1 1.6-2.6 2.2-4.4 1.4-3.6-1.6-6.1-4.1-7.6-7.8-.7-1.9-.2-3.5 1.1-4.5z" fill="#1a5fb4"/></svg>
    <div>Call Us on<strong>000-555-0142</strong></div>
  </div>
  <nav class="abs main-nav">
    <a class="active" href="#" style="left:0">WELCOME</a>
    <a href="#" style="left:91px">OUR COMMUNITIES</a>
    <a href="#" style="left:230px">AMMENITIES</a>
    <a href="#" style="left:332px">FITTING</a>
    <a href="#" style="left:408px">EVENTS</a>
    <a href="#" style="left:485px">ABOUT US</a>
    <a href="#" style="left:576px">CONTACT</a>
  </nav>
</header>

<section>
  <div class="abs photo hero-kitchen" role="img" aria-label="Bright kitchen with wooden cabinets and a dining table by large windows"></div>
  <div class="abs photo hero-bed1" role="img" aria-label="Furnished bedroom with neutral bedding"></div>
  <div class="abs photo hero-living" role="img" aria-label="Sunny living room with rug and sofa"></div>
  <div class="abs photo hero-bed2" role="img" aria-label="Bedroom with wood ceiling and grey bedding"></div>
  <div class="abs hero-banner">
    <svg class="arrows" viewBox="0 0 30 24" aria-hidden="true"><path d="M9 5 3 12l6 7M21 5l6 7-6 7" fill="none" stroke="#fff" stroke-width="2"/></svg>
    <p>ROOM RENTAL STARTING AT <b>2500</b> <small>/month</small></p>
  </div>
</section>

<section>
  <h1 class="abs section-title welcome-title">Welcome to <em>Harbor Nest Lodging</em></h1>
  <div class="abs title-rule welcome-rule"></div>
  <p class="abs welcome-copy">Traditional apartments and housing rentals are a thing of the past. We have created an all-encompassing living experience that aligns perfectly with your trendy, yet sophisticated lifestyle. Harbor Nest Lodging is unlike anything you have ever experienced before. We invite you to explore our selection of home communities and discover the passion we have for providing wonderful experiencesSed ut perspiciatis unde omnis iste natus error sit voluptatem accusantium doloremque laudantium, totam rem aperiam, eaque ipsa quae ab illo inventore veritatis et quasi architecto beatae vitae dicta sunt</p>
  <a class="abs btn btn-contact" href="#">Contact Us</a>
</section>

<section class="abs amenities">
  <div class="abs amenities-photo" role="img" aria-label="Warm lit bedroom with upholstered headboard and bedside lamps"></div>
  <h2 class="abs section-title amenities-title">Luxurious Amenities<sup>*</sup></h2>
  <div class="abs amenities-rule"></div>
  <ul class="abs amenity-list amenity-col1">
    <li><svg viewBox="0 0 11 11"><circle cx="5.5" cy="5.5" r="5.5" fill="#1a5fb4"/><path d="m4.3 3 2.5 2.5-2.5 2.5" fill="none" stroke="#fff" stroke-width="1.4"/></svg>High-speed Wi-Fi</li>
    <li><svg viewBox="0 0 11 11"><circle cx="5.5" cy="5.5" r="5.5" fill="#1a5fb4"/><path d="m4.3 3 2.5 2.5-2.5 2.5" fill="none" stroke="#fff" stroke-width="1.4"/></svg>All inclusive utilities (with Green Cap)</li>
    <li><svg viewBox="0 0 11 11"><circle cx="5.5" cy="5.5" r="5.5" fill="#1a5fb4"/><path d="m4.3 3 2.5 2.5-2.5 2.5" fill="none" stroke="#fff" stroke-width="1.4"/></svg>Optional enclosed garage</li>
    <li><svg viewBox="0 0 11 11"><circle cx="5.5" cy="5.5" r="5.5" fill="#1a5fb4"/><path d="m4.3 3 2.5 2.5-2.5 2.5" fill="none" stroke="#fff" stroke-width="1.4"/></svg>Fully furnished kitchen</li>
    <li><svg viewBox="0 0 11 11"><circle cx="5.5" cy="5.5" r="5.5" fill="#1a5fb4"/><path d="m4.3 3 2.5 2.5-2.5 2.5" fill="none" stroke="#fff" stroke-width="1.4"/></svg>Washer and dryer</li>
    <li><svg viewBox="0 0 11 11"><circle cx="5.5" cy="5.5" r="5.5" fill="#1a5fb4"/><path d="m4.3 3 2.5 2.5-2.5 2.5" fill="none" stroke="#fff" stroke-width="1.4"/></svg>Spacious, newly updated rooms</li>
  </ul>
  <ul class="abs amenity-list amenity-col2">
    <li><svg viewBox="0 0 11 11"><circle cx="5.5" cy="5.5" r="5.5" fill="#1a5fb4"/><path d="m4.3 3 2.5 2.5-2.5 2.5" fill="none" stroke="#fff" stroke-width="1.4"/></svg>Private use, full bath with each room</li>
    <li><svg viewBox="0 0 11 11"><circle cx="5.5" cy="5.5" r="5.5" fill="#1a5fb4"/><path d="m4.3 3 2.5 2.5-2.5 2.5" fill="none" stroke="#fff" stroke-width="1.4"/></svg>Bi-monthly community events</li>
    <li><svg viewBox="0 0 11 11"><circle cx="5.5" cy="5.5" r="5.5" fill="#1a5fb4"/><path d="m4.3 3 2.5 2.5-2.5 2.5" fill="none" stroke="#fff" stroke-width="1.4"/></svg>Various networking event invitations, well suited&nbsp; for young professionals</li>
  </ul>
</section>

<section>
  <article class="abs highlight col-home">
    <h3 class="section-title">Home <em>with HNL</em></h3>
    <div class="rule"></div>
    <div class="photo photo-home" role="img" aria-label="Living room with hardwood floor and large windows"></div>
    <p>Sedperspiciatis unde omnis iste natus error sit voltatem accusantium doloremque laudantium, totam rem aperiam, eaque ipsa quae ab illo inventore veritatis et quasi architecto beatae vitae dicta sSedperspias und omnis iste natus error sit voluptatem accusan</p>
    <a class="btn btn-more" href="#">Read more <svg viewBox="0 0 9 9"><circle cx="4.5" cy="4.5" r="4.5" fill="#fff"/><path d="m3.5 2.3 2.2 2.2-2.2 2.2" fill="none" stroke="#1a5fb4" stroke-width="1.2"/></svg></a>
  </article>
  <article class="abs highlight col-events">
    <h3 class="section-title">Most <em>Recent Events</em></h3>
    <div class="rule"></div>
    <div class="photo photo-events" role="img" aria-label="Group of young friends enjoying a party at home"></div>
    <p>Sedperspiciatis unde omnis iste natus error sit voltatem accusantium doloremque laudantium, totam rem aperiam, eaque ipsa quae ab illo inventore veritatis et quasi architecto beatae vitae dicta sSedperspias und omnis iste natus error sit voluptatem accusan</p>
    <a class="btn btn-more" href="#">Read more <svg viewBox="0 0 9 9"><circle cx="4.5" cy="4.5" r="4.5" fill="#fff"/><path d="m3.5 2.3 2.2 2.2-2.2 2.2" fill="none" stroke="#1a5fb4" stroke-width="1.2"/></svg></a>
  </article>
  <article class="abs highlight col-latest">
    <h3 class="section-title">Our <em>Latest Addition</em></h3>
    <div class="rule"></div>
    <div class="photo photo-latest" role="img" aria-label="Newly added bedroom with wood ceiling and grey bedding"></div>
    <p>Sedperspiciatis unde omnis iste natus error sit voltatem accusantium doloremque laudantium, totam rem aperiam, eaque ipsa quae ab illo inventore veritatis et quasi architecto beatae vitae dicta sSedperspias und omnis iste natus error sit voluptatem accusan</p>
    <a class="btn btn-more" href="#">Read more <svg viewBox="0 0 9 9"><circle cx="4.5" cy="4.5" r="4.5" fill="#fff"/><path d="m3.5 2.3 2.2 2.2-2.2 2.2" fill="none" stroke="#1a5fb4" stroke-width="1.2"/></svg></a>
  </article>
</section>

<section class="abs fans">
  <h2 class="abs section-title fans-title">Our <em>Fans</em></h2>
  <div class="abs title-rule fans-rule"></div>
  <div class="abs avatar avatar-1" role="img" aria-label="Portrait of resident Marco"></div>
  <p class="abs quote quote-1">I thought I wanted to live on my own, but the reality is I just didn't want to go through he hassle of finding a good room mate. Someone with common interests that's not out partying at night. I'm a professional and don't need that in my life. Now I'm a part of a great social, athletic, professional community that encourages the most out of me.</p>
  <div class="abs fan-name fan-1">MARCO, 30</div>
  <div class="abs avatar avatar-2" role="img" aria-label="Portrait of resident Priya"></div>
  <p class="abs quote quote-2">People are social creatures. It's simply a human trait. Whether we are introverts or extroverts, shy or gregarious, we need to know that we are part of a common group. We need to feel that we have others with whom we connect and who share commonalities. I love feeling accepted as a piece of a greater puzzle where we look out for each other, support each other's needs.</p>
  <div class="abs fan-name fan-2">PRIYA,</div>
</section>

<footer class="abs site-footer">
  <div class="abs footer-brand"><span class="mark"></span><span>Harbor Nest Lodging</span></div>
  <p class="abs footer-about">Sed ut perspiciatis unde omnis isten error sit voluptatem accusantiloudo emq ue laudantiu totavolupt</p>
  <div class="abs footer-col col-resources">
    <h4>Resources</h4>
    <a href="#">Support</a><a href="#">Security Center</a><a href="#">Developer Center</a><a href="#">Shopping Carts</a><a href="#">Legal</a>
  </div>
  <div class="abs footer-col col-support">
    <h4>Support</h4>
    <a href="#">FAQs</a><a href="#">Privacy Policy</a><a href="#">Recommendations</a><a href="#">Contact</a>
  </div>
  <div class="abs footer-col col-news">
    <h4>Sign Up Newsletter</h4>
    <p>Please sign up here for latest deals</p>
    <span class="email-field">Email address</span>
    <span class="btn-subscribe">Subscribe</span>
  </div>
</footer>

<div class="abs bottom-bar">
  <p class="abs copyright">Copyright © 2016&nbsp; All Rights Reserved. HarborNestLodging.example</p>
  <nav class="abs social" aria-label="Social links">
    <a href="#" aria-label="Video channel"></a>
    <a href="#" aria-label="Social profile"></a>
    <a href="#" aria-label="Photo feed"></a>
    <a href="#" aria-label="chirpnet"></a>
    <a href="#" aria-label="Community page"></a>
  </nav>
</div>

</body>
</html>
```